I need a business card design for my streamora channel called The Plain Kettle Show. I make streamora cooking tutorials. I'd like the phrase " Keep the kettle warm, more to cook soon" somewhere on the BC. The Streamora web address is www.streamora.example/user/PlainKettleShow
email - promos@zentaclip.example
Updates
I have just updated what i am looking for on the card. Thanks
Industry/Entity Type
Cooking
Contact Information for Business Card
The name of my business is The Plain Kettle Show. It's a Streamora channel & the url is https://www.streamora.example/user/PlainKettleShow
Am am a StreamOra partner.
My name is Marcus.
Logo Text
The Plain Kettle Show
Logo styles of interest
Pictorial/Combination Logo
Look and feel
Each slider illustrates characteristics of the customer's brand and the style your logo design should communicate.

```html
<!DOCTYPE html>
<html lang="en">
<head>
<meta charset="utf-8">
<title>The Plain Kettle Show – Business Card</title>
<link href="https://fonts.googleapis.com/css2?family=PT+Sans:wght@400;700&display=swap" rel="stylesheet">
<style>
  :root {
    --page: #ecebe8;
    --card: #ffffff;
    --orange: #f7931e;
    --orange-deep: #f68b1f;
    --yellow: #fff23a;
    --amber: #fbb03b;
    --red: #f15a5a;
    --ink-white: #ffffff;
    --rule-dark: #6b5a48;
  }
  * { box-sizing: border-box; margin: 0; padding: 0; }
  html, body {
    width: 1200px; height: 1000px; overflow: hidden;
    background: var(--page);
    font-family: "PT Sans", sans-serif;
  }
  .canvas { position: relative; width: 1200px; height: 1000px; }
  .card {
    position: absolute; left: 220px;
    width: 760px; height: 420px;
    background: var(--card);
    border-radius: 34px;
    overflow: hidden;
    box-shadow: 0 6px 18px rgba(0,0,0,.18);
  }
  .card--front { top: 50px; }
  .card--back { top: 530px; }

  .top-rule {
    position: absolute; left: 0; right: 0; height: 5px;
    background: linear-gradient(90deg, var(--amber), var(--orange), var(--red));
    border-top: 1px solid var(--rule-dark);
  }
  .card--front .top-rule { top: 52px; }
  .card--back .top-rule { top: 26px; }

  .band {
    position: absolute; left: 0; right: 0; height: 58px;
    background: linear-gradient(90deg, var(--yellow) 0%, var(--amber) 35%, var(--orange) 70%, var(--red) 100%);
    border-top: 1px solid var(--rule-dark);
    border-bottom: 1px solid var(--rule-dark);
  }
  .card--front .band { bottom: 36px; }
  .card--back .band { bottom: 48px; }

  /* Front */
  .front-title {
    position: absolute; top: 120px; left: 0; right: 0;
    text-align: center; color: var(--orange);
    font-size: 44px; font-weight: 400; line-height: 1.1;
  }
  .contact-email {
    position: absolute; top: 270px; left: 0; right: 0;
    display: flex; justify-content: center; align-items: center; gap: 10px;
    color: var(--orange-deep); font-weight: 700; font-size: 22px;
  }
  .contact-email svg { width: 30px; height: 30px; }
  .band-content {
    position: absolute; inset: 0;
    display: flex; align-items: center; gap: 14px; padding-left: 36px;
    color: var(--ink-white); font-weight: 700;
  }
  .platform-name { font-size: 24px; }
  .platform-url { font-size: 24px; }

  /* Back */
  .show-mark {
    position: absolute; top: 70px; left: 60px;
    display: flex; align-items: center; gap: 16px;
  }
  .show-mark__square { width: 60px; height: 60px; background: var(--orange); flex: none; }
  .show-mark__name {
    color: var(--orange); font-size: 30px; font-weight: 700; line-height: 1.1;
    width: 190px;
  }
  .sign-off {
    position: absolute; top: 120px; left: 330px; width: 400px;
    text-align: center; color: var(--orange);
    font-size: 36px; line-height: 1.15;
  }
</style>
</head>
<body>
<main class="canvas">
  <section class="card card--front" aria-label="Card front">
    <div class="top-rule"></div>
    <h1 class="front-title">The Plain Kettle Show<br>Marcus</h1>
    <p class="contact-email">
      <svg viewBox="0 0 30 30" aria-hidden="true">
        <circle cx="15" cy="15" r="14" fill="#fbb03b"/>
        <rect x="7" y="9.5" width="16" height="11" fill="#fff" stroke="#333" stroke-width="1.2"/>
        <path d="M7 9.5 L15 16 L23 9.5" fill="none" stroke="#333" stroke-width="1.2"/>
      </svg>
      email - promos@zentaclip.example
    </p>
    <div class="band">
      <div class="band-content">
        <span class="platform-name">Streamora</span>
        <span class="platform-url">www.streamora.example/user/PlainKettleShow</span>
      </div>
    </div>
  </section>

  <section class="card card--back" aria-label="Card back">
    <div class="top-rule"></div>
    <div class="show-mark">
      <span class="show-mark__square"></span>
      <span class="show-mark__name">The Plain Kettle Show</span>
    </div>
    <p class="sign-off">" Keep the kettle warm,<br>more to cook soon"</p>
    <div class="band"></div>
  </section>
</main>
</body>
</html>
```